Paintless Dent Company need a Fresh new look on a SUV partial wrap The company is named "Hull...

We are a Paintless Dent Company named Hull Mend.
Our logo is on our Facebook page. That logo needs to be on both sides along with 1. hail repair 2. ding and dent repair 3. 317-555-0148

```html
<!DOCTYPE html>
<html lang="en">
<head>
<meta charset="utf-8">
<title>Hull Mend – SUV Partial Wrap</title>
<link rel="stylesheet" href="https://fonts.googleapis.com/css2?family=Montserrat:ital,wght@0,800;1,700&display=swap">
<style>
  :root {
    --bg: #f4f4f4;
    --band-dark: #2b2b2d;
    --band-red: #d92b35;
    --stripe: #ffffff;
    --ink-dark: #1e1e20;
    --ink-light: #ffffff;
  }
  html, body {
    margin: 0;
    padding: 0;
    width: 1200px;
    height: 665px;
    overflow: hidden;
    background: var(--bg);
  }
  .wrap-design {
    display: block;
    width: 1200px;
    height: 665px;
  }
  .band-dark { fill: var(--band-dark); }
  .band-red { fill: var(--band-red); }
  .band-stripe { fill: var(--stripe); }
  .brand-name {
    font-family: "Montserrat", sans-serif;
    font-weight: 800;
    font-size: 56px;
    letter-spacing: 22px;
    fill: var(--ink-dark);
  }
  .brand-dot { fill: var(--ink-dark); }
  .services {
    font-family: "Montserrat", sans-serif;
    font-style: italic;
    font-weight: 700;
    font-size: 32px;
    letter-spacing: 2px;
    fill: var(--ink-light);
  }
  .phone {
    font-family: "Montserrat", sans-serif;
    font-style: italic;
    font-weight: 700;
    font-size: 28px;
    letter-spacing: 2px;
    fill: var(--ink-light);
  }
</style>
</head>
<body>
<svg class="wrap-design" viewBox="0 0 1200 665" xmlns="http://www.w3.org/2000/svg" aria-label="Hull Mend side wrap graphic">
  <rect width="1200" height="665" fill="var(--bg)"/>

  <g class="wrap-graphic" transform="rotate(-12.6 600 340)">
    <!-- diagonal bands -->
    <rect class="band-dark" x="100" y="318" width="1300" height="82"/>
    <rect class="band-stripe" x="380" y="400" width="1020" height="7"/>
    <rect class="band-red" x="380" y="407" width="1020" height="64"/>

    <!-- brand name -->
    <rect class="brand-dot" x="150" y="262" width="24" height="24"/>
    <text class="brand-name" x="196" y="290">HULL MEND?</text>

    <!-- services -->
    <text class="services" x="300" y="372">• Hail Repair&#160;&#160;&#160;• Ding and Dent Repair</text>

    <!-- phone -->
    <text class="phone" x="560" y="449">317-555-0148</text>
  </g>
</svg>
</body>
</html>
```